Redesign of an insurance website

Attached is an insurance website that I need to redesign. Currently the website is too dark. I like for example www.brambleshield.com . Could you make the website lighter and change the structure a little so that it is more user friendly?

Industry/Entity Type

Insurance

Number of Pages Required

4 page

```html
<!DOCTYPE html>
<html lang="cs">
<head>
<meta charset="utf-8">
<title>Jistotnik.cz – Insurance</title>
<link rel="stylesheet" href="https://fonts.googleapis.com/css2?family=PT+Sans:wght@400;700&display=swap">
<style>
  :root{
    --page:#f6f7fb;
    --ink:#1f2740;
    --muted:#8a91a6;
    --label:#9aa1b2;
    --divider:#dde1ea;
    --accent:#2f86fb;
    --accent-soft:#e7f0ff;
    --scene-light:#fbf3ef;
    --scene-cool:#e4ebf7;
    --scene-warm:#f3dcd4;
  }
  *{box-sizing:border-box;margin:0;padding:0}
  html,body{width:1200px;height:619px;overflow:hidden}
  body{font-family:"PT Sans",sans-serif;color:var(--ink);background:var(--page)}
  .hero{position:relative;width:1200px;height:619px;overflow:hidden}
  .hero-backdrop{
    position:absolute;inset:0;
    background:
      radial-gradient(ellipse 640px 260px at 600px 110px, var(--scene-warm), transparent 70%),
      radial-gradient(ellipse 420px 380px at 1080px 470px, var(--scene-cool), transparent 75%),
      linear-gradient(180deg, var(--scene-light) 0%, #f5f2f6 45%, var(--scene-cool) 100%);
  }
  .topbar{position:absolute;left:26px;right:30px;top:20px;height:40px;display:flex;justify-content:space-between;align-items:center}
  .brand{font-weight:700;font-size:21px;letter-spacing:1.6px;color:var(--ink)}
  .login{font-size:17px;color:var(--ink);text-decoration:none;padding:6px 14px;border:1px solid var(--divider);border-radius:4px;background:rgba(255,255,255,.7)}
  .headline{position:absolute;top:174px;left:0;width:100%;text-align:center;font-weight:400;font-size:53px;line-height:64px;letter-spacing:.3px;color:var(--ink)}
  .products{position:absolute;top:272px;left:0;width:100%;height:90px}
  .arrow{position:absolute;top:28px}
  .product{position:absolute;text-align:center;transform:translateX(-50%);color:var(--muted);font-size:16px;line-height:20px;white-space:nowrap}
  .product svg{display:block;margin:0 auto 6px}
  .product.is-active{color:var(--ink)}
  .signup{position:absolute;left:225px;top:386px;width:750px;height:56px;background:#fff;border-radius:5px;display:flex;overflow:hidden;box-shadow:0 8px 24px rgba(31,39,64,.12);border:1px solid var(--divider)}
  .field{position:relative;height:100%;padding:15px 0 0 37px}
  .field + .field::before{content:"";position:absolute;left:0;top:18px;height:22px;border-left:1px solid var(--divider)}
  .field-first{width:187px}
  .field-last{width:189px;padding-left:10px}
  .field-email{flex:1;padding-left:10px}
  .field label{display:block;font-size:8.5px;color:var(--label);margin-bottom:3px}
  .field span{font-size:11px;color:var(--ink)}
  .cta{width:186px;background:var(--accent);color:#fff;border:0;font-family:inherit;font-size:14.5px;display:flex;align-items:center;justify-content:space-between;padding:0 18px 0 24px;letter-spacing:.3px}
</style>
</head>
<body>
<main class="hero">
  <div class="hero-backdrop" role="img" aria-label="Soft light photo of a driver's hands on a steering wheel with city lights"></div>

  <header class="topbar">
    <div class="brand">JISTOTNIK.CZ</div>
    <a class="login" href="#">Login/Sign In</a>
  </header>

  <h1 class="headline">Indulge. Infer. Insure.</h1>

  <nav class="products" aria-label="Insurance types">
    <svg class="arrow" style="left:383px" width="14" height="24" viewBox="0 0 14 24"><path d="M11 2 2 12l9 10" fill="none" stroke="#8a91a6" stroke-width="2.4"/></svg>
    <div class="product" style="left:481px;top:10px">
      <svg width="42" height="30" viewBox="0 0 42 30" fill="none" stroke="#8a91a6" stroke-width="1.5">
        <path d="M2 22h14l2-6h8l4 6h10"/><circle cx="10" cy="24" r="3"/><circle cx="32" cy="24" r="3"/>
        <path d="M21 12l-3-6 4 3 2-7 2 7 4-3-3 6"/>
      </svg>
      Accident
    </div>
    <div class="product is-active" style="left:600px;top:6px">
      <svg width="90" height="46" viewBox="0 0 90 46" fill="none" stroke="#1f2740" stroke-width="3.2" stroke-linejoin="round">
        <path d="M4 34V24q0-4 5-5l12-2 10-12q3-3 8-3h18q5 0 8 4l7 10 9 2q4 1 4 5v11H71m-38 0h20m-33 0H4"/>
        <circle cx="27" cy="36" r="6"/><circle cx="66" cy="36" r="6"/>
      </svg>
      Car Insurance
    </div>
    <div class="product" style="left:719px;top:12px">
      <svg width="30" height="28" viewBox="0 0 30 28" fill="none" stroke="#8a91a6" stroke-width="1.5">
        <path d="M3 2h24l2 8H1z"/><path d="M3 10v16h24V10"/><path d="M7 26v-9h6v9M16 16h7v5h-7z"/>
      </svg>
      Business
    </div>
    <svg class="arrow" style="left:804px" width="14" height="24" viewBox="0 0 14 24"><path d="M3 2l9 10-9 10" fill="none" stroke="#8a91a6" stroke-width="2.4"/></svg>
  </nav>

  <form class="signup">
    <div class="field field-first"><label>First name</label><span>Jméno</span></div>
    <div class="field field-last"><label>Last name</label><span>Příjmení</span></div>
    <div class="field field-email"><label>E-mail</label><span>info@jistotnik.cz</span></div>
    <button class="cta" type="button">SPOČÍTAT CENU
      <svg width="14" height="10" viewBox="0 0 14 10"><path d="M0 5h12M8 1l4 4-4 4" fill="none" stroke="#fff" stroke-width="1.3"/></svg>
    </button>
  </form>
</main>
</body>
</html>
```